I would like a formal monogram with MR and Marlena Rosk Interiors written somehow. this a a new interior design company based in Dallas. My favorite colors is Halvorn blue with gold or white writing or some variation of.
back: Marlena Rosk
214-555-0163
marlena.rosk@fernmail.example
www.marlenaroskinteriors.example

```html
<!DOCTYPE html>
<html lang="en">
<head>
<meta charset="utf-8">
<title>Marlena Rosk Interiors – Business Card</title>
<link rel="stylesheet" href="https://fonts.googleapis.com/css2?family=Cinzel:wght@400&family=Roboto:wght@300&display=swap">
<style>
  :root {
    --backdrop: #2c2c2d;
    --card-dark: #151617;
    --card-light: #2b2c2e;
    --teal: #129c95;
    --gold-dark: #8a6424;
    --gold-light: #e2bb52;
    --text-light: #d9d9d9;
  }
  * { margin: 0; padding: 0; box-sizing: border-box; }
  html, body {
    width: 1200px; height: 1138px; overflow: hidden;
    background: var(--backdrop);
  }
  .card {
    position: absolute;
    left: 273px; width: 621px;
    border-radius: 16px;
    overflow: hidden;
    background: linear-gradient(135deg, var(--card-dark) 0%, #1d1e20 55%, var(--card-light) 100%);
    box-shadow: 0 6px 14px rgba(0,0,0,0.45);
  }
  .card--front { top: 184px; height: 376px; }
  .card--back { top: 606px; height: 375px; }

  .brand-mark {
    position: absolute;
    border: 2px solid var(--teal);
    border-radius: 50%;
  }
  .brand-name {
    position: absolute;
    font-family: "Cinzel", serif;
    font-weight: 400;
    color: var(--teal);
    text-align: center;
    white-space: nowrap;
  }
  .card--front .brand-mark { left: 269px; top: 88px; width: 84px; height: 84px; }
  .card--front .brand-name { left: 0; width: 100%; top: 196px; font-size: 34px; letter-spacing: 1px; }

  .web-line {
    position: absolute; top: 334px; left: 0; width: 100%;
    display: flex; justify-content: center; align-items: center; gap: 18px;
    font-family: "Roboto", sans-serif; font-weight: 300;
    font-size: 16px; color: var(--text-light);
  }
  .web-line .rule {
    width: 86px; height: 2px;
    background: linear-gradient(90deg, transparent, var(--gold-light) 50%, var(--gold-dark));
  }
  .web-line .rule--right {
    background: linear-gradient(90deg, var(--gold-dark), var(--gold-light) 50%, transparent);
  }
  .accent-band {
    position: absolute; left: 0; bottom: 0; width: 100%; height: 12px;
    display: flex;
  }
  .accent-band .teal { flex: 1; background: var(--teal); }
  .accent-band .gold {
    flex: 1;
    background: linear-gradient(90deg, var(--gold-dark), var(--gold-light) 45%, var(--gold-dark));
  }

  .card--back .brand-mark { left: 130px; top: 108px; width: 70px; height: 70px; }
  .card--back .brand-name { left: 20px; width: 290px; top: 198px; font-size: 23px; line-height: 1.25; }

  .contact-name {
    position: absolute; left: 332px; top: 118px;
    font-family: "Cinzel", serif; font-size: 24px; color: var(--teal);
  }
  .contact-list {
    position: absolute; left: 332px; top: 184px;
    list-style: none;
    font-family: "Roboto", sans-serif; font-weight: 300;
    font-size: 17px; color: var(--text-light);
  }
  .contact-list li {
    display: flex; align-items: center; gap: 14px; height: 24px;
  }
  .contact-list svg { width: 16px; height: 16px; fill: var(--teal); flex: none; }
</style>
</head>
<body>
  <section class="card card--front">
    <div class="brand-mark" aria-hidden="true"></div>
    <div class="brand-name">MARLENA ROSK INTERIORS</div>
    <div class="web-line">
      <span class="rule"></span>
      <span class="web-address">www.marlenaroskinteriors.example</span>
      <span class="rule rule--right"></span>
    </div>
    <div class="accent-band"><span class="teal"></span><span class="gold"></span></div>
  </section>

  <section class="card card--back">
    <div class="brand-mark" aria-hidden="true"></div>
    <div class="brand-name">MARLENA ROSK<br>INTERIORS</div>
    <div class="contact-name">MARLENA ROSK</div>
    <ul class="contact-list">
      <li>
        <svg viewBox="0 0 16 16" aria-hidden="true"><path d="M2 5c0-2 3-3 6-3s6 1 6 3v1h-3V5H5v1H2z M4 7h8l2 6H2z"/></svg>
        214-555-0163
      </li>
      <li>
        <svg viewBox="0 0 16 16" aria-hidden="true"><path d="M1 3h14v10H1z M2 4l6 5 6-5" fill="var(--teal)"/><path d="M2 4.5l6 5 6-5" fill="none" stroke="#1d1e20" stroke-width="1.2"/></svg>
        marlena.rosk@fernmail.example
      </li>
      <li>
        <svg viewBox="0 0 16 16" aria-hidden="true"><circle cx="8" cy="8" r="7"/><path d="M1 8h14M8 1v14M3 4.5h10M3 11.5h10" stroke="#1d1e20" stroke-width="0.9" fill="none"/><ellipse cx="8" cy="8" rx="3" ry="7" fill="none" stroke="#1d1e20" stroke-width="0.9"/></svg>
        marlenaroskinteriors.example
      </li>
    </ul>
  </section>
</body>
</html>
```